Nail Technician Business Card Design

My business is a nail technician business which involves applying nail enhancements to clients nails. I would like a design that uses the colours:, purple or black and silver on a light grey background. The final design should entice clients to my business.
I would like appointment times on the back of the card.
I want the spilled bottle on the front and the other one on the back
I would like the dragonfly font
Updates
Project Deadline Extended
Reason: I have found a font I would like used and also an image/logo
I have listed some ideas I would like used on the design of my card. thanks
Tessa
Industry/Entity Type
Business
Contact Information for Business Card
Lumen Nail Designs
41 Wendover street,
Marrowby, NSW 2871
Mobile: 0400 582 316
Tessa Harcourt
Like us on Friendloop
Font styles to use
Other font styles liked:
- Dragonfly
Look and feel
Each slider illustrates characteristics of the customer's brand and the style your logo design should communicate.

```html
<!DOCTYPE html>
<html lang="en">
<head>
<meta charset="utf-8">
<title>Lumen Nail Designs – Business Card</title>
<link rel="stylesheet" href="https://fonts.googleapis.com/css2?family=Courgette&display=swap">
<style>
  :root {
    --backdrop: #e6e6e8;
    --card-white: #ffffff;
    --pattern-grey: #e9e8ec;
    --plum: #b02a9a;
    --plum-bright: #c93fb2;
    --band-purple: #8e1f7c;
    --ink-black: #0d0d0f;
    --damask-dark: #1c1c20;
    --text-white: #f4f2f5;
    --script: "Courgette", cursive;
  }
  * { box-sizing: border-box; margin: 0; padding: 0; }
  html, body {
    width: 1200px;
    height: 900px;
    overflow: hidden;
    background: var(--backdrop);
  }
  .canvas {
    position: relative;
    width: 1200px;
    height: 900px;
  }
  .card {
    position: absolute;
    left: 100px;
    top: 164px;
    width: 1000px;
    height: 572px;
    border-radius: 30px;
    overflow: hidden;
    background: var(--card-white);
  }
  .card__pattern {
    position: absolute;
    inset: 0 0 auto 0;
    height: 262px;
    background: linear-gradient(180deg, var(--card-white) 0%, var(--pattern-grey) 55%, var(--card-white) 100%);
  }
  .card__lower {
    position: absolute;
    left: 0;
    right: 0;
    top: 262px;
    bottom: 0;
    background: radial-gradient(ellipse at 70% 40%, var(--damask-dark) 0%, var(--ink-black) 75%);
  }
  .card__band {
    position: absolute;
    left: 0;
    top: 240px;
    width: 1000px;
    height: 40px;
  }
  .brand {
    position: absolute;
    left: 72px;
    top: 108px;
    display: flex;
    align-items: center;
    gap: 16px;
  }
  .brand__dot {
    width: 22px;
    height: 22px;
    border-radius: 50%;
    background: var(--plum);
    flex: none;
  }
  .brand__name {
    font-family: var(--script);
    font-weight: 400;
    font-size: 50px;
    line-height: 60px;
    color: var(--plum);
    white-space: nowrap;
  }
  .product-photo {
    position: absolute;
    left: 660px;
    top: 0;
    width: 300px;
    height: 235px;
    background: linear-gradient(200deg, var(--ink-black) 0%, #3a1035 30%, var(--plum-bright) 62%, #e07ad0 80%, var(--card-white) 100%);
    border-radius: 0 0 40px 40px;
  }
  .contact {
    position: absolute;
    left: 72px;
    top: 318px;
    font-family: var(--script);
    font-size: 34px;
    line-height: 60px;
    color: var(--text-white);
    white-space: nowrap;
  }
  .contact__label,
  .contact__social { color: var(--plum-bright); }
</style>
</head>
<body>
<main class="canvas">
  <article class="card">
    <div class="card__pattern" role="img" aria-label="Faint line pattern of nail polish bottles and brushes"></div>
    <div class="card__lower" role="img" aria-label="Dark damask ornament pattern"></div>

    <svg class="card__band" viewBox="0 0 1000 40" aria-hidden="true">
      <path d="M0 22 Q500 12 1000 4 L1000 14 Q500 22 0 32 Z" fill="var(--band-purple)"/>
    </svg>

    <div class="brand">
      <span class="brand__dot" aria-hidden="true"></span>
      <h1 class="brand__name">Lumen Nail Designs</h1>
    </div>

    <div class="product-photo" role="img" aria-label="Photo of an open magenta nail polish bottle spilling polish"></div>

    <div class="contact">
      <p><span class="contact__label">Addres:</span> 41 Wendover street, Marrowby, NSW 2871</p>
      <p><span class="contact__label">Mobile:</span> 0400 582 316</p>
      <p>Tessa Harcourt <span class="contact__social">Like us on Friendloop</span></p>
    </div>
  </article>
</main>
</body>
</html>
```